One page flyer for nonprofit focused IT company

I need a one page flyer (one side of a single 8.5x11 page) with text and graphics. The company logo is already done, and it must appear on the flyer along with other icons and graphics. The final design will be printed on heavy weight glossy paper as a handout and also distributed as a PDF.

The text is provided in an attachment, if it needs to be shortened let me know.

Industry/Entity Type

Information Technology

Requirements
Must have
• some flare (colors, icons or images)
Should not have
• While we work for nonprofits, my company is a FOR PROFIT company.

```html
<!DOCTYPE html>
<html lang="en">
<head>
<meta charset="UTF-8">
<title>Meridian Data Corporation – Nonprofit IT Flyer</title>
<link href="https://fonts.googleapis.com/css2?family=Montserrat:wght@500;600;700;800&family=Roboto:ital,wght@0,400;0,500;1,700&display=swap" rel="stylesheet">
<style>
  :root{
    --maroon:#951b2b;
    --maroon-dark:#7d1524;
    --white:#ffffff;
    --ink:#2b2b2b;
    --photo-dark:#151b27;
    --photo-mid:#2e3546;
  }
  *{margin:0;padding:0;box-sizing:border-box}
  html,body{width:869px;height:1200px;overflow:hidden;background:var(--white)}
  .flyer{position:relative;width:869px;height:1200px;background:var(--white);font-family:"Roboto",Arial,sans-serif;color:var(--ink)}
  .shapes{position:absolute;left:0;top:0}
  .abs{position:absolute}
  .heading{font-family:"Montserrat",Arial,sans-serif;font-weight:700;text-transform:uppercase}

  .brand{left:299px;top:14px;width:271px;text-align:center;display:flex;align-items:center;justify-content:center;gap:7px;
    font-family:"Montserrat",Arial,sans-serif;font-weight:700;font-size:12px;color:var(--maroon);letter-spacing:.3px;flex-direction:column}
  .brand-mark{width:30px;height:30px;background:var(--maroon)}

  .intro-title{left:173px;top:296px;width:523px;text-align:center;color:var(--white);font-size:15.5px;line-height:21px}
  .intro-body{left:215px;top:355px;width:440px;text-align:center;color:#e8e8ee;font-size:11.4px;line-height:15.5px}

  .stat-number{left:62px;top:460px;color:var(--white);font-family:"Montserrat",Arial,sans-serif;font-weight:800;font-size:104px;line-height:1;letter-spacing:-3px}
  .stat-label{left:64px;top:564px;color:var(--white);font-size:24px;line-height:33px}

  .section-title{font-family:"Montserrat",Arial,sans-serif;font-weight:800;font-size:36px;line-height:1;text-transform:uppercase}
  .successes-title{left:134px;top:656px;color:var(--white)}
  .solutions-title{left:540px;top:556px;color:var(--maroon)}

  .success-head{left:114px;width:300px;color:var(--white);font-size:15px;line-height:20px}
  .success-body{left:62px;width:339px;color:#f6e9eb;font-size:11.4px;line-height:15.5px;text-align:justify}
  .success-body em{font-weight:700}

  .solution-head{left:516px;color:var(--maroon);font-size:15px;line-height:20px}
  .solution-body{left:475px;width:353px;color:var(--ink);font-size:11.4px;line-height:15.5px;text-align:justify}
  .solution-body.short{text-align:left}

  .contact{left:453px;top:1133px;width:416px;height:56px;background:var(--maroon);border-radius:18px 0 0 18px;color:var(--white);padding:9px 0 0 20px}
  .contact-lead{font-size:12.5px;line-height:18px}
  .contact-line{font-family:"Montserrat",Arial,sans-serif;font-size:13.5px;line-height:19px;font-weight:700}
  .contact-line .or{font-weight:500;font-size:12px}
</style>
</head>
<body>
<main class="flyer">

  <svg class="shapes" width="869" height="1200" viewBox="0 0 869 1200" aria-hidden="true">
    <defs>
      <linearGradient id="photoTone" x1="0" y1="0" x2="0" y2="1">
        <stop offset="0" stop-color="#2c3446"/>
        <stop offset=".5" stop-color="#1c2230"/>
        <stop offset="1" stop-color="#10141d"/>
      </linearGradient>
    </defs>
    <polygon points="129,0 740,0 740,418 435,554 129,426" fill="var(--maroon)"/>
    <polygon points="27,384 435,554 435,1200 27,1200" fill="var(--maroon)"/>
  </svg>

  <svg class="abs" style="left:173px;top:0" width="523" height="506" viewBox="0 0 523 506" role="img" aria-label="Photo of a businessman in a dark suit holding a glowing world map network of connected people">
    <polygon points="0,0 523,0 523,399 262,506 0,399" fill="url(#photoTone)"/>
  </svg>

  <svg class="abs" style="left:299px;top:0" width="271" height="104" viewBox="0 0 271 104" aria-hidden="true">
    <polygon points="0,0 271,0 271,55 135.5,103 0,55" fill="var(--white)"/>
  </svg>
  <div class="abs brand"><span class="brand-mark"></span>MERIDIAN DATA CORPORATION</div>

  <h2 class="abs heading intro-title">An efficient and elegant approach<br>to IT solution implementations</h2>
  <p class="abs intro-body">Meridian Data Corporation has been supporting the Information Systems needs of nonprofits for over 50 years. We continually strive to bring the latest technologies and best practices to nonprofits to drive down the cost of IT while implementing systems that drive revenue.</p>

  <div class="abs stat-number">50</div>
  <div class="abs heading stat-label">Years of nonprofit<br>IT services</div>

  <svg class="abs" style="left:64px;top:647px" width="54" height="54" viewBox="0 0 54 54" aria-hidden="true">
    <circle cx="27" cy="27" r="25" fill="none" stroke="#fff" stroke-width="2"/>
    <circle cx="24" cy="17" r="4.5" fill="#fff"/>
    <path d="M16 36 q0-11 8-11 q8 0 8 11z" fill="#fff"/>
    <polyline points="14,40 22,33 28,37 39,26" fill="none" stroke="#fff" stroke-width="2.2"/>
    <polyline points="34,26 39,26 39,31" fill="none" stroke="#fff" stroke-width="2.2"/>
  </svg>
  <h2 class="abs section-title successes-title">Successes</h2>

  <svg class="abs" style="left:65px;top:721px" width="32" height="32" viewBox="0 0 32 32" aria-hidden="true">
    <circle cx="16" cy="16" r="15" fill="none" stroke="#fff" stroke-width="1.6"/>
    <path d="M9 9v14h15" fill="none" stroke="#fff" stroke-width="1.6"/>
    <rect x="12" y="12" width="2.5" height="10" fill="#fff"/><rect x="16" y="15" width="2.5" height="7" fill="#fff"/><rect x="20" y="18" width="2.5" height="4" fill="#fff"/>
  </svg>
  <h3 class="abs heading success-head" style="top:717px">90% reduction in software<br>development costs</h3>
  <p class="abs success-body" style="top:766px">Regional Auto Dealers Council Vehicle Value Guide needed to update its core product they engaged their in-house IT department who estimated the project would take 3 years and cost $3,000,000. RADC decided to work with Meridian Data Corporation instead, and the product was released to production in only 9 months at <em>one-tenth of the cost</em>, only $300,000</p>

  <svg class="abs" style="left:65px;top:888px" width="32" height="32" viewBox="0 0 32 32" aria-hidden="true">
    <circle cx="16" cy="16" r="15" fill="none" stroke="#fff" stroke-width="1.6"/>
    <rect x="9" y="19" width="3" height="5" fill="#fff"/><rect x="14" y="15" width="3" height="9" fill="#fff"/><rect x="19" y="11" width="3" height="13" fill="#fff"/>
    <polyline points="8,16 14,11 20,8 24,7" fill="none" stroke="#fff" stroke-width="1.4"/>
  </svg>
  <h3 class="abs heading success-head" style="top:894px">10x increase in membership</h3>
  <p class="abs success-body" style="top:928px">Open Pathways Conservancy needed to move to online membership registration and contracted with Meridian Data Corporation to build a significant online presence to engage potential members. Through compelling online tools and mobile applications, Open Pathways has <em>increased membership 10 fold.</em></p>

  <svg class="abs" style="left:65px;top:1032px" width="32" height="32" viewBox="0 0 32 32" aria-hidden="true">
    <circle cx="16" cy="16" r="15" fill="none" stroke="#fff" stroke-width="1.6"/>
    <path d="M9 9v14h15" fill="none" stroke="#fff" stroke-width="1.6"/>
    <rect x="12" y="13" width="2.5" height="9" fill="#fff"/><rect x="16" y="16" width="2.5" height="6" fill="#fff"/><rect x="20" y="12" width="2.5" height="10" fill="#fff"/>
  </svg>
  <h3 class="abs heading success-head" style="top:1038px">20% reduction in overhead</h3>
  <p class="abs success-body" style="top:1072px">The National Civic Leaders Alliance had antiquated systems in place to manage over 500 chapters across the nation. Meridian Data Corporation developed online tools to allow communication and management between the local chapters and national headquarters. This eliminated much of the overhead of chapter management, <em>reducing HR costs by 20%.</em></p>

  <svg class="abs" style="left:466px;top:547px" width="54" height="54" viewBox="0 0 54 54" aria-hidden="true">
    <circle cx="27" cy="27" r="25" fill="none" stroke="var(--maroon)" stroke-width="2"/>
    <path d="M21 30 q-4-4-4-9 a10 10 0 0 1 20 0 q0 5-4 9v4h-12z" fill="none" stroke="var(--maroon)" stroke-width="2"/>
    <line x1="22" y1="38" x2="32" y2="38" stroke="var(--maroon)" stroke-width="2"/>
    <line x1="24" y1="42" x2="30" y2="42" stroke="var(--maroon)" stroke-width="2"/>
    <path d="M27 7v3M12 12l2 2M42 12l-2 2M8 21h3M43 21h3" stroke="var(--maroon)" stroke-width="2"/>
  </svg>
  <h2 class="abs section-title solutions-title">Solutions</h2>

  <svg class="abs" style="left:474px;top:618px" width="30" height="30" viewBox="0 0 30 30" aria-hidden="true">
    <circle cx="15" cy="15" r="14" fill="none" stroke="var(--maroon)" stroke-width="1.6"/>
    <rect x="8" y="9" width="14" height="10" rx="1" fill="none" stroke="var(--maroon)" stroke-width="1.5"/>
    <line x1="12" y1="22" x2="18" y2="22" stroke="var(--maroon)" stroke-width="1.5"/>
  </svg>
  <h3 class="abs heading solution-head" style="top:624px">Web applications</h3>
  <p class="abs solution-body" style="top:656px">With a focus on non-profit websites and web based applications, MDC helps nonprofits communicate with their members and donors while maximizing online giving and engagement</p>

  <svg class="abs" style="left:474px;top:714px" width="30" height="30" viewBox="0 0 30 30" aria-hidden="true">
    <circle cx="15" cy="15" r="14" fill="none" stroke="var(--maroon)" stroke-width="1.6"/>
    <rect x="10" y="7" width="10" height="16" rx="1.5" fill="none" stroke="var(--maroon)" stroke-width="1.5"/>
    <circle cx="15" cy="20" r="1" fill="var(--maroon)"/>
  </svg>
  <h3 class="abs heading solution-head" style="top:720px">Mobile applications</h3>
  <p class="abs solution-body" style="top:747px">Meridian Data Corporation implements mobile applications for every major mobile platform to provide direct communications with members and donors enabling real-time, two-way interaction</p>

  <svg class="abs" style="left:474px;top:807px" width="30" height="30" viewBox="0 0 30 30" aria-hidden="true">
    <circle cx="15" cy="15" r="14" fill="none" stroke="var(--maroon)" stroke-width="1.6"/>
    <circle cx="15" cy="15" r="6" fill="none" stroke="var(--maroon)" stroke-width="3" stroke-dasharray="3 2"/>
    <circle cx="15" cy="15" r="2" fill="var(--maroon)"/>
  </svg>
  <h3 class="abs heading solution-head" style="top:813px">Systems integration</h3>
  <p class="abs solution-body" style="top:842px">IT applications can get scattered and disconnected. Meridian Data Corporation has decades of experience integrating these applications into a single cohesive system.</p>

  <svg class="abs" style="left:474px;top:898px" width="30" height="30" viewBox="0 0 30 30" aria-hidden="true">
    <circle cx="15" cy="15" r="14" fill="none" stroke="var(--maroon)" stroke-width="1.6"/>
    <ellipse cx="15" cy="9" rx="7" ry="2.5" fill="none" stroke="var(--maroon)" stroke-width="1.5"/>
    <path d="M8 9v12c0 1.5 3 2.5 7 2.5s7-1 7-2.5V9M8 13c0 1.5 3 2.5 7 2.5s7-1 7-2.5M8 17c0 1.5 3 2.5 7 2.5s7-1 7-2.5" fill="none" stroke="var(--maroon)" stroke-width="1.5"/>
  </svg>
  <h3 class="abs heading solution-head" style="top:904px">Member donor database</h3>
  <p class="abs solution-body" style="top:932px">Meridian Data Corporation's Quillory Member / Donor CRM system is fully customized for each client meeting the unique needs of your organization</p>

  <svg class="abs" style="left:474px;top:991px" width="30" height="30" viewBox="0 0 30 30" aria-hidden="true">
    <circle cx="15" cy="15" r="14" fill="none" stroke="var(--maroon)" stroke-width="1.6"/>
    <path d="M9 19a4 4 0 0 1 1-8 5 5 0 0 1 9.5-1 4 4 0 0 1 1 9z" fill="none" stroke="var(--maroon)" stroke-width="1.5"/>
    <path d="M12 19v4M15 19v5M18 19v4" stroke="var(--maroon)" stroke-width="1.4"/>
  </svg>
  <h3 class="abs heading solution-head" style="top:997px">Cloud migration</h3>
  <p class="abs solution-body short" style="top:1024px">Reduce IT costs by migrating to the latest cloud solutions</p>

  <svg class="abs" style="left:474px;top:1055px" width="30" height="30" viewBox="0 0 30 30" aria-hidden="true">
    <circle cx="15" cy="15" r="14" fill="none" stroke="var(--maroon)" stroke-width="1.6"/>
    <ellipse cx="15" cy="9" rx="7" ry="2.5" fill="none" stroke="var(--maroon)" stroke-width="1.5"/>
    <path d="M8 9v12c0 1.5 3 2.5 7 2.5s7-1 7-2.5V9M8 13c0 1.5 3 2.5 7 2.5s7-1 7-2.5M8 17c0 1.5 3 2.5 7 2.5s7-1 7-2.5" fill="none" stroke="var(--maroon)" stroke-width="1.5"/>
  </svg>
  <h3 class="abs heading solution-head" style="top:1050px">Business intelligence<br>and reporting</h3>
  <p class="abs solution-body" style="top:1093px">Meridian Data Corporation can wrestle all of an organization's data into simple executive dashboards and reports</p>

  <div class="abs contact">
    <p class="contact-lead">Contact Meridian Data Corporation at</p>
    <p class="contact-line">info@meridiandatacorp.com <span class="or">or</span> 555-014-2200 x417</p>
  </div>

</main>
</body>
</html>
```